Property Management business needs Business cards designed

We provide a premium property management service based in Sydney's Norther Beaches. We want people to feel confident in choosing us to manage their investment properties. We offer a much more personalized service than other estate agents.
We want a modern clean design. Something that shows confidence without being complicated.
Logo attached.

Target Market(s)

35-70yo Male and Female with strong property portfolios within Sydney's Norther Beaches

Industry/Entity Type

Property Management

Contact Information for Business Card

Address: Suite 7, 12-14 Kelvin Parade, Harlow NSW 2188
Two separate named cards.
Tom Ardley - 0491 570 118 tom@harbourvaleestates.com.au
Clara Dunmore - 0491 570 263 clara@harbourvaleestates.com.au

Requirements
Must have
• Business logo, name, number, address, email.

```html
<!DOCTYPE html>
<html lang="en">
<head>
<meta charset="utf-8">
<title>Harbourvale Estates – Business Cards</title>
<link rel="stylesheet" href="https://fonts.googleapis.com/css2?family=Arimo:wght@400&family=PT+Sans:wght@400;700&display=swap">
<style>
  :root {
    --backdrop: #cfd7d9;
    --card: #eef2f3;
    --card-edge: #dfe6e8;
    --ink: #1c1f22;
    --teal: #35a9b6;
    --white: #ffffff;
  }
  * { margin: 0; padding: 0; box-sizing: border-box; }
  html, body {
    width: 1200px;
    height: 1034px;
    overflow: hidden;
    background: var(--backdrop);
  }
  .canvas {
    position: relative;
    width: 1200px;
    height: 1034px;
  }
  .card {
    position: absolute;
    left: 240px;
    width: 720px;
    height: 464px;
    background: var(--card);
    border: 1px solid var(--card-edge);
    border-radius: 17px;
    box-shadow: 0 8px 26px rgba(40, 60, 65, 0.18);
  }
  .card-tom   { top: 38px; }
  .card-clara { top: 532px; }

  .brand {
    position: absolute;
    left: 26px;
    top: 128px;
    display: flex;
    align-items: center;
    gap: 11px;
    font-family: "PT Sans", sans-serif;
    font-weight: 700;
    font-size: 36px;
    line-height: 1;
    letter-spacing: 0.4px;
    color: var(--ink);
    white-space: nowrap;
  }
  .brand-mark {
    width: 20px;
    height: 20px;
    background: var(--teal);
  }
  .line {
    position: absolute;
    right: 46px;
    display: flex;
    align-items: center;
    gap: 20px;
    line-height: 1.2;
    white-space: nowrap;
  }
  .name {
    font-family: "Arimo", sans-serif;
    font-size: 32px;
    color: var(--teal);
  }
  .detail {
    font-family: "PT Sans", sans-serif;
    font-size: 21px;
    color: var(--ink);
  }
  .icon {
    width: 15px;
    height: 15px;
    display: block;
    flex: none;
  }
  .name    { top: 176px; }
  .phone   { top: 236px; }
  .email   { top: 270px; }
  .address { top: 304px; }
</style>
</head>
<body>
<div class="canvas">

  <div class="card card-tom">
    <div class="brand"><span class="brand-mark"></span>HARBOURVALE ESTATES</div>
    <div class="line name">Tom Ardley</div>
    <div class="line detail phone">0491 570 118
      <svg class="icon" viewBox="0 0 17 17" aria-hidden="true"><rect width="17" height="17" fill="var(--teal)"/><path d="M4 5.5h9v2H11v-1H6v1H4z M5.5 8h6l1 4h-8z" fill="var(--white)"/></svg>
    </div>
    <div class="line detail email">tom@harbourvaleestates.com.au
      <svg class="icon" viewBox="0 0 17 17" aria-hidden="true"><rect width="17" height="17" fill="var(--teal)"/><rect x="3.5" y="5" width="10" height="7" fill="var(--white)"/><path d="M3.5 5l5 4 5-4" fill="none" stroke="var(--teal)" stroke-width="1"/></svg>
    </div>
    <div class="line detail address">Suite 7, 12-14 Kelvin Parade, Harlow NSW 2188
      <svg class="icon" viewBox="0 0 17 17" aria-hidden="true"><rect width="17" height="17" fill="var(--teal)"/><path d="M8.5 3.5a3.2 3.2 0 0 1 3.2 3.2c0 2.4-3.2 6.3-3.2 6.3s-3.2-3.9-3.2-6.3a3.2 3.2 0 0 1 3.2-3.2z" fill="var(--white)"/><circle cx="8.5" cy="6.7" r="1.2" fill="var(--teal)"/></svg>
    </div>
  </div>

  <div class="card card-clara">
    <div class="brand"><span class="brand-mark"></span>HARBOURVALE ESTATES</div>
    <div class="line name">Clara Dunmore</div>
    <div class="line detail phone">0491 570 263
      <svg class="icon" viewBox="0 0 17 17" aria-hidden="true"><rect width="17" height="17" fill="var(--teal)"/><path d="M4 5.5h9v2H11v-1H6v1H4z M5.5 8h6l1 4h-8z" fill="var(--white)"/></svg>
    </div>
    <div class="line detail email">clara@harbourvaleestates.com.au
      <svg class="icon" viewBox="0 0 17 17" aria-hidden="true"><rect width="17" height="17" fill="var(--teal)"/><rect x="3.5" y="5" width="10" height="7" fill="var(--white)"/><path d="M3.5 5l5 4 5-4" fill="none" stroke="var(--teal)" stroke-width="1"/></svg>
    </div>
    <div class="line detail address">Suite 7, 12-14 Kelvin Parade, Harlow NSW 2188
      <svg class="icon" viewBox="0 0 17 17" aria-hidden="true"><rect width="17" height="17" fill="var(--teal)"/><path d="M8.5 3.5a3.2 3.2 0 0 1 3.2 3.2c0 2.4-3.2 6.3-3.2 6.3s-3.2-3.9-3.2-6.3a3.2 3.2 0 0 1 3.2-3.2z" fill="var(--white)"/><circle cx="8.5" cy="6.7" r="1.2" fill="var(--teal)"/></svg>
    </div>
  </div>

</div>
</body>
</html>
```